75%-100% OFF - Insulation Banner Design

Need banners created for an online marketing push for my insulation business Velmoor Energy.

www.velmoorenergy.com

Specifically - I would like the banners to pop utilizing our colors in neon. To see samples of colors we use - visit our asset folder.

https://files.quarnex.com/share/7hTkw29plDfa0XbmQzRv4uYc8JnG3sLe?view=open

I will attach sample files to this project.

The banner must highlight 75%-100% off Insulation and Weatherization. If you can include our current perfect Brivvo reviews somewhere in the advertisement that would be awesome but not a requirement.

The banner must meet Kettle Rebate logo guidelines. Please see attachment.

Target Market(s)

Home Owners

Industry/Entity Type

Insulation and Construction

Font styles to use
Sans Serif

Colors
59FF00
82FF00
B8FF75
E3FFCB
F4FFEA

Requirements
Must have
• Kettle Rebate Logo per project description. Must have 75-100% off somewhere that is very clear. And must have our company Velmoor Energy Logo.
Nice to have
• Velmoor Energy Logo

```html
<!DOCTYPE html>
<html lang="en">
<head>
<meta charset="utf-8">
<title>Velmoor Energy Banners</title>
<link rel="stylesheet" href="https://fonts.googleapis.com/css2?family=Anton&family=Jost:wght@400;500&family=Poppins:wght@600;700&display=swap">
<style>
  :root {
    --page: #f3f3f3;
    --neon: #7ed321;
    --neon-bright: #82ff00;
    --neon-soft: #b8ff75;
    --mint: #eef6e2;
    --mint-pale: #f4ffea;
    --ink: #1a1a1a;
    --grey: #555;
    --partner: #3b6b1f;
    --white: #ffffff;
  }
  * { box-sizing: border-box; margin: 0; padding: 0; }
  html, body { width: 1004px; height: 1200px; overflow: hidden; background: var(--page); }
  body { position: relative; font-family: "Jost", sans-serif; }

  .banner { position: absolute; left: 68px; width: 868px; height: 496px; overflow: hidden; box-shadow: 0 2px 10px rgba(0,0,0,.08); }
  .banner--hero { top: 75px; }
  .banner--welcome { top: 629px; background: linear-gradient(135deg, #f6fbef 0%, #eaf5da 60%, #f2f9e8 100%); }

  .brand-mark { position: absolute; color: var(--white); font-family: "Jost", sans-serif; font-weight: 500; white-space: nowrap; z-index: 2; }
  .offer { position: absolute; z-index: 2; height: 26px; padding: 0 14px; border-radius: 13px; background: var(--neon-bright);
    font-family: "Poppins", sans-serif; font-weight: 700; font-size: 12.5px; line-height: 26px; color: var(--ink); white-space: nowrap; }

  /* Hero banner */
  .hero-photo { position: absolute; left: 0; top: 0; width: 868px; height: 409px;
    background: linear-gradient(160deg, #8a4a22 0%, #b86a35 30%, #c9a27a 55%, #d8c29e 75%, #bfa47c 100%); }
  .hero-photo::after { content: ""; position: absolute; inset: 0; background: rgba(60,30,10,.2); }
  .banner--hero .brand-mark { left: 0; width: 868px; top: 26px; text-align: center; font-size: 30px; }
  .hero-headline { position: absolute; left: 0; width: 868px; top: 192px; text-align: center; z-index: 2;
    font-family: "Anton", sans-serif; font-weight: 400; font-size: 28px; line-height: 34px; color: var(--white); letter-spacing: .2px; }
  .hero-services { position: absolute; left: 0; width: 868px; top: 276px; text-align: center; z-index: 2;
    font-family: "Poppins", sans-serif; font-weight: 700; font-size: 12px; color: var(--white); }
  .hero-services .sep { margin: 0 13px; }
  .banner--hero .offer { left: 50%; transform: translateX(-50%); top: 312px; }

  .contact-bar { position: absolute; left: 0; top: 409px; width: 868px; height: 87px; background: var(--mint); }
  .contact-icon { position: absolute; top: 26px; width: 34px; height: 34px; border-radius: 50%; background: var(--neon);
    display: flex; align-items: center; justify-content: center; }
  .contact-label { position: absolute; font-family: "Poppins", sans-serif; font-weight: 600; font-size: 11.5px; color: var(--ink); }
  .contact-value { position: absolute; font-size: 10.5px; line-height: 15px; color: var(--grey); white-space: nowrap; }
  .partner { position: absolute; font-family: "Jost", sans-serif; font-weight: 500; color: var(--partner); white-space: nowrap; }

  /* Welcome banner */
  .welcome-art { position: absolute; inset: 0; }
  .welcome-title { position: absolute; left: 298px; top: 72px; font-family: "Anton", sans-serif; font-weight: 400; font-size: 23px; color: var(--white); z-index: 2; }
  .banner--welcome .brand-mark { left: 622px; top: 75px; font-size: 20px; }
  .welcome-headline { position: absolute; left: 461px; top: 184px; font-family: "Poppins", sans-serif;
    font-weight: 700; font-size: 15px; line-height: 21px; color: var(--ink); white-space: nowrap; }
  .welcome-headline span { display: block; }
  .welcome-headline span:nth-child(2) { margin-left: 11px; }
  .welcome-headline span:nth-child(3) { margin-left: 23px; }
  .service-list { position: absolute; left: 502px; top: 270px; list-style: none; }
  .service-list li { display: flex; align-items: center; gap: 12px; height: 31px; font-size: 14.5px; color: #444; }
  .service-list li:nth-child(2) { margin-left: 13px; }
  .service-list li:nth-child(3) { margin-left: 26px; }
  .banner--welcome .offer { left: 508px; top: 370px; }
</style>
</head>
<body>

<section class="banner banner--hero">
  <div class="hero-photo" role="img" aria-label="Photo of a worker in protective gear laying insulation batts between attic rafters"></div>
  <div class="brand-mark">Velmoor Energy</div>
  <h1 class="hero-headline">WE CAN HELP YOU SAVE ON YOUR ENERGY BILLS BY<br>IMPROVING YOUR ENERGY EFFICIENCY</h1>
  <p class="hero-services">HOME ENERGY ASSESSMENTS<span class="sep">|</span>INSULATION &amp; AIR SEALING<span class="sep">|</span>VIRTUAL ASSESSMENTS</p>
  <p class="offer">75%–100% OFF INSULATION &amp; WEATHERIZATION</p>

  <div class="contact-bar">
    <div class="contact-icon" style="left:80px">
      <svg width="16" height="18" viewBox="0 0 16 18"><path d="M8 1a5 5 0 0 0-5 5c0 4 5 9 5 9s5-5 5-9a5 5 0 0 0-5-5z" fill="none" stroke="#fff" stroke-width="1.6"/><circle cx="8" cy="6" r="1.8" fill="#fff"/><path d="M3 16.5h10" stroke="#fff" stroke-width="1.4"/></svg>
    </div>
    <div class="contact-label" style="left:128px;top:16px">ADDRESS:</div>
    <div class="contact-value" style="left:127px;top:38px">42 Harrow Lane, Suite B2,<br>Fairhaven, MA 02719</div>

    <div class="contact-icon" style="left:275px">
      <svg width="18" height="13" viewBox="0 0 18 13"><rect x="1" y="1" width="16" height="11" rx="1.5" fill="#fff"/><path d="M1.5 2l7.5 5.5L16.5 2" fill="none" stroke="#7ed321" stroke-width="1.4"/></svg>
    </div>
    <div class="contact-label" style="left:323px;top:23px">EMAIL:</div>
    <div class="contact-value" style="left:322px;top:46px">info@velmoorenergy.com</div>

    <div class="contact-icon" style="left:442px">
      <svg width="17" height="17" viewBox="0 0 17 17"><path d="M4 1.5l2.5 3-1.5 2c1 2 3 4 5 5l2-1.5 3 2.5-1.5 2.5C8 16 1 9 1.5 3z" fill="none" stroke="#fff" stroke-width="1.5" stroke-linejoin="round"/></svg>
    </div>
    <div class="contact-label" style="left:490px;top:23px">PHONE:</div>
    <div class="contact-value" style="left:489px;top:46px">555-014-2290</div>

    <div class="partner" style="left:600px;top:28px;font-size:22px">Brivvo</div>
    <div class="partner" style="left:712px;top:32px;font-size:16px">Kettle Rebate</div>
  </div>
</section>

<section class="banner banner--welcome">
  <svg class="welcome-art" width="868" height="496" viewBox="0 0 868 496">
    <defs>
      <linearGradient id="photoTone" x1="0" y1="0" x2="1" y2="1">
        <stop offset="0" stop-color="#8c5a33"/>
        <stop offset=".35" stop-color="#c98b52"/>
        <stop offset=".6" stop-color="#e0c58f"/>
        <stop offset="1" stop-color="#c9a066"/>
      </linearGradient>
    </defs>
    <polygon points="0,0 341,0 552,496 0,496" fill="#b8ff75"/>
    <polygon points="0,0 335,0 545,496 0,496" fill="url(#photoTone)" role="img" aria-label="Photo of a worker in a red cap and overalls fitting insulation between attic rafters beside a skylight"/>
    <polygon points="248,48 787,48 787,141 288,141" fill="#b8ff75"/>
    <polygon points="242,42 781,42 781,135 282,135" fill="#7ed321"/>
  </svg>
  <h2 class="welcome-title">WELCOME TO VELMOOR ENERGY</h2>
  <div class="brand-mark">Velmoor Energy</div>
  <p class="welcome-headline"><span>WE CAN HELP YOU SAVE ON YOUR ENERGY</span><span>BILLS BY IMPROVING YOUR ENERGY</span><span>EFFICIENCY</span></p>
  <ul class="service-list">
    <li><svg width="14" height="14" viewBox="0 0 14 14"><circle cx="7" cy="7" r="7" fill="#7ed321"/><path d="M4 7h6M7.5 4.2L10.3 7 7.5 9.8" fill="none" stroke="#fff" stroke-width="1.8"/></svg>Home Energy Assessments</li>
    <li><svg width="14" height="14" viewBox="0 0 14 14"><circle cx="7" cy="7" r="7" fill="#7ed321"/><path d="M4 7h6M7.5 4.2L10.3 7 7.5 9.8" fill="none" stroke="#fff" stroke-width="1.8"/></svg>Insulation &amp; Air Sealing</li>
    <li><svg width="14" height="14" viewBox="0 0 14 14"><circle cx="7" cy="7" r="7" fill="#7ed321"/><path d="M4 7h6M7.5 4.2L10.3 7 7.5 9.8" fill="none" stroke="#fff" stroke-width="1.8"/></svg>Virtual Assessments</li>
  </ul>
  <p class="offer">75%–100% OFF INSULATION &amp; WEATHERIZATION</p>
  <div class="partner" style="left:564px;top:412px;font-size:24px">Brivvo</div>
  <div class="partner" style="left:700px;top:418px;font-size:17px">Kettle Rebate</div>
</section>

</body>
</html>
```